Flyer Design Project

We want to design a flyer for a laundromat in San Francisco. It will be used to market the services of the laundromat. I am uploading a .jpg file with details to be highlighted. The flyer should be of size 8.5 in x 11 in and should be attractive and hard hitting. The attachment should only be used for the copy, not for design.

Target Market(s)

Laundromat and laundry users

Requirements
Must have
• Must have a attention grabbing headline
Nice to have
• Pictures

```html
<!DOCTYPE html>
<html lang="en">
<head>
<meta charset="utf-8">
<title>Harbor Lane Laundromat Flyer</title>
<link rel="stylesheet" href="https://fonts.googleapis.com/css2?family=Oswald:wght@500;700&family=Montserrat:wght@500;600;700&family=Questrial&display=swap">
<style>
:root{
  --backdrop:#1e1f22;
  --navy:#0b3a66;
  --navy-deep:#08284a;
  --blue:#0f5c9a;
  --sky:#2c8fd3;
  --ink:#2a2a2a;
  --headline:#e6f36b;
  --paper:#ffffff;
  --coupon:#e4e7ea;
}
*{box-sizing:border-box;margin:0;padding:0}
html,body{width:1200px;height:777px;overflow:hidden;background:var(--backdrop)}
.page{position:absolute;top:41px;width:525px;height:680px;background:var(--paper);overflow:hidden;font-family:"Questrial",sans-serif;color:var(--ink)}
.page-front{left:53px}
.page-back{left:614px}
.abs{position:absolute}
.center{text-align:center}

/* front */
.hero{left:0;top:0;width:525px;height:258px;background:linear-gradient(180deg,#0e4f86 0%,#1f78bd 55%,#6fb6e6 100%)}
.headline{left:0;top:10px;width:525px;white-space:nowrap;font-family:"Oswald",sans-serif;font-weight:700;font-size:33px;letter-spacing:0;color:var(--headline);text-shadow:0 2px 3px rgba(0,0,0,.35)}
.qa{width:240px}
.qa h3{font-family:"Montserrat",sans-serif;font-weight:600;font-size:11.5px;color:var(--blue);line-height:1.25;letter-spacing:.2px}
.qa p{font-size:9.5px;line-height:1.4;margin-top:2px}
.coupon{width:146px;height:94px;background:linear-gradient(180deg,#f4f5f6,var(--coupon));border:1.5px dashed #7a8a99;outline:4px solid #f0f2f4}
.coupon .big{font-family:"Oswald",sans-serif;font-weight:500;font-size:32px;color:var(--blue);line-height:1;margin-top:4px}
.coupon .txt{font-size:11px;line-height:1.3;margin-top:3px}
.coupon .valid{position:absolute;left:10px;bottom:6px;font-family:"Montserrat",sans-serif;font-weight:600;font-size:9px}
.loc h3{font-family:"Montserrat",sans-serif;font-weight:600;font-size:11.5px;color:var(--blue)}
.loc p{font-size:9.2px;margin-top:3px}
.footer-band{left:0;width:525px;height:52px;background:linear-gradient(180deg,var(--blue),var(--navy-deep))}
.brand{border:2px solid #fff;border-radius:8px;background:linear-gradient(180deg,#15609e,var(--navy-deep));display:flex;align-items:center;gap:8px;padding-left:8px}
.brand-dot{width:42px;height:42px;border-radius:50%;background:#c9d3db;flex:none}
.brand-name{font-family:"Questrial",sans-serif;font-size:16px;line-height:1.05;color:#fff}
.web{font-family:"Oswald",sans-serif;font-weight:500;color:var(--navy);font-size:17px}
.call{font-family:"Oswald",sans-serif;font-weight:500;color:#fff;font-size:28px;letter-spacing:.5px;white-space:nowrap}

/* back */
.top-band{left:0;top:0;width:525px;height:52px;background:linear-gradient(180deg,var(--navy-deep),var(--blue))}
.tag{left:142px;top:19px;width:240px;height:32px;border:2px solid var(--navy);border-radius:8px;background:#fff;font-family:"Montserrat",sans-serif;font-weight:600;font-size:16px;color:var(--navy);display:flex;align-items:center;justify-content:center}
.col{width:158px}
.col h4{font-family:"Montserrat",sans-serif;font-weight:600;font-size:10px;color:var(--blue);text-align:center}
.col .photo{width:148px;height:82px;margin:5px auto 0;border-radius:4px}
.col h5{font-family:"Montserrat",sans-serif;font-weight:600;font-size:9px;text-align:center;margin-top:14px;line-height:1.3;white-space:nowrap}
.col .body{font-size:8.2px;line-height:1.4;margin-top:14px}
.col ul{list-style:none;margin-top:8px}
.col li{position:relative;padding-left:10px;margin-bottom:8px}
.col li::before{content:"•";position:absolute;left:0;color:var(--sky)}
.col p+p{margin-top:8px}
.small{font-size:6.5px}
.loyalty{left:15px;top:392px;width:495px;height:63px;border-radius:8px;background:linear-gradient(180deg,var(--blue),var(--navy-deep));padding:3px}
.loyalty-inner{width:100%;height:100%;border:1px dashed rgba(255,255,255,.7);border-radius:6px;color:#fff;text-align:center;padding-top:8px}
.loyalty-inner .l1{font-family:"Montserrat",sans-serif;font-weight:600;font-size:15.5px}
.loyalty-inner .l2{font-size:16px;margin-top:2px}
.mission{left:18px;top:478px;width:196px;text-align:center;color:var(--blue)}
.mission h3{font-family:"Montserrat",sans-serif;font-weight:600;font-size:19px;color:var(--navy)}
.mission p{font-size:12.2px;line-height:1.3;margin-top:2px}
.store{left:218px;top:474px;width:281px;height:89px;border-radius:4px;background:linear-gradient(180deg,#dfe8f2 0%,#dfe8f2 18%,#3c4a58 18%,#5c6a78 60%,#2b3440 100%)}
.addr{font-size:7.8px;line-height:1.35}
.addr strong{font-family:"Montserrat",sans-serif;font-weight:600;font-size:11px;color:var(--navy);display:block}
.addr b{font-family:"Montserrat",sans-serif;font-weight:600}
.web-back{font-family:"Montserrat",sans-serif;font-weight:600;font-size:10.5px;color:#fff}
.call-back{font-family:"Montserrat",sans-serif;font-weight:600;font-size:22px;color:#fff;white-space:nowrap}
</style>
</head>
<body>

<section class="page page-front">
  <div class="abs hero" role="img" aria-label="Laundromat interior with washing machines, a laundry basket, a blue wave and water bubbles with a green leaf"></div>
  <h1 class="abs headline center">FAST FORWARD YOUR LAUNDRY DAY!</h1>

  <div class="abs qa center" style="left:18px;top:270px">
    <h3>NO TIME FOR GROCERY SHOPPING?</h3>
    <p>Do you grocery shopping at nearby Greenleaf Market while our machines do your laundry</p>
  </div>
  <div class="abs qa center" style="left:18px;top:326px">
    <h3>HAVE LARGE LAUNDRY LOADS?</h3>
    <p>Bring them in your car: we have ample parking</p>
  </div>
  <div class="abs qa center" style="left:18px;top:372px">
    <h3>TIRED OF WASHING YOUR CLOTHES<br>IN A DIRTY LAUNDROMAT?</h3>
    <p>We have the cleanest Laundromat in the bay area with efficient attendants</p>
  </div>
  <div class="abs qa center" style="left:270px;top:270px">
    <h3>HATE DOING LAUDRY?</h3>
    <p>We will fast forward you day with our large commercial washers and dryers: you will be out of here in no time</p>
  </div>
  <div class="abs qa center" style="left:270px;top:333px">
    <h3>GET BORED DOING LAUNDRY?</h3>
    <p>Not here! We have free Wi-Fi and flat screen tv to keep you entertained</p>
  </div>
  <div class="abs qa center" style="left:270px;top:388px">
    <h3>NO TIME FOR LAUNDRY?</h3>
    <p>Bring it to us and collect it washed, folded and neatly packed after 24 hours.</p>
  </div>

  <div class="abs coupon center" style="left:108px;top:441px">
    <div class="big">FREE WASH</div>
    <div class="txt">One Load of 20 LB<br><b>Wash Free</b> with this</div>
    <div class="valid">coupon valid:</div>
  </div>
  <div class="abs coupon center" style="left:269px;top:441px">
    <div class="big">50% OFF</div>
    <div class="txt">On you First Wash<br>and Fold Order</div>
    <div class="valid">coupon valid:</div>
  </div>

  <div class="abs loc center" style="left:0;top:548px;width:525px">
    <h3>OUR LOCATION IS A MULTI TASKERS DREAM:</h3>
    <p>Grocery shopping at nearby Greenleaf Market, lunch at Jade Wok (our Hero Deli or Bayou Chicken) coffee at Morning Cup</p>
  </div>

  <div class="abs footer-band" style="top:628px"></div>
  <div class="abs brand" style="left:13px;top:602px;width:164px;height:62px">
    <span class="brand-dot"></span>
    <span class="brand-name">harbor lane<br>laundromat</span>
  </div>
  <div class="abs web center" style="left:190px;top:603px;width:330px">www.HarborLaneLaundry.com</div>
  <div class="abs call center" style="left:190px;top:632px;width:330px">Call us Now: 415.555.0182</div>
</section>

<section class="page page-back">
  <div class="abs top-band"></div>
  <div class="abs tag">OUR LAUNDRY SOLUTION</div>

  <div class="abs col" style="left:12px;top:64px">
    <h4>FULL SERVICE WASH, DRY</h4>
    <div class="photo" style="background:linear-gradient(180deg,#cfd6dd,#6c7783 55%,#8f979f)" role="img" aria-label="Row of stainless steel washing machines"></div>
    <h5>You are busy so WE will<br>wash, dry and fold for YOU</h5>
    <div class="body">
      <p>When you drop your clothes off, we operate in the following sequence:</p>
      <ul>
        <li>Your clothes are sorted and colors separated from whites.</li>
        <li>Your clothes are washed and dried in separate machines for each customer, according to your preferences indicated to our attendant.</li>
        <li>Your clothes are neatly folded, socks matched and everything packed nice and tidy.</li>
      </ul>
    </div>
  </div>

  <div class="abs col" style="left:184px;top:64px">
    <h4>SELF-SERVICE</h4>
    <div class="photo" style="background:linear-gradient(180deg,#b7c7d6,#d9a36c 55%,#e8d27a)" role="img" aria-label="Couple holding laundry in front of washers"></div>
    <h5>Express coin operated washers<br>and dryers of all sizes</h5>
    <div class="body">
      <p>We have 35 high speed energy and water saving washers, from 10 lb capacity to 60 lb capacity.</p>
      <p>Our dryers are efficient and HOT! And we have 16 stacks of 2 dryers each</p>
      <p>And our attendant is available to assist you to select the best washer for your needs. Please ask in case you need any assistance.</p>
    </div>
  </div>

  <div class="abs col" style="left:356px;top:64px">
    <h4>COMMERCIAL ACCOUNTS</h4>
    <div class="photo" style="background:linear-gradient(180deg,#e4e8ec,#a5adb6 55%,#c9ced3)" role="img" aria-label="Bright laundromat hall with folding tables"></div>
    <h5>For Hotels, Nursing Homes,<br>Sports Clubs, Schools etc</h5>
    <div class="body">
      <p>If you run a Hotel, Nursing home, Sports Club, School etc and regularly have large loads to wash, you may open a commercial account with us.</p>
      <p>With a Commercial account you will have the following benefits:</p>
      <ul>
        <li>Commercial discounts</li>
        <li>Free laundry bag</li>
        <li>Monthly invoicing <span class="small">(after credit approval) (your first order should be prepaid)</span></li>
      </ul>
    </div>
  </div>

  <div class="abs loyalty">
    <div class="loyalty-inner">
      <div class="l1">HARBOR LANE LAUNDROMAT LOYALTY PROGRAM</div>
      <div class="l2">AVAIL 60 MINUTES OF FREE DRYER TIME ON YOUR 11TH VISIT</div>
    </div>
  </div>

  <div class="abs mission">
    <h3>Our Mission:</h3>
    <p>To provide an immaculately clean laundromat with friendly service where doing laundry becomes a pleasant pastime</p>
  </div>
  <div class="abs store" role="img" aria-label="Laundromat storefront with shop sign"></div>

  <div class="abs footer-band" style="top:637px"></div>
  <div class="abs brand" style="left:21px;top:591px;width:167px;height:62px">
    <span class="brand-dot"></span>
    <span class="brand-name">harbor lane<br>laundromat</span>
  </div>
  <div class="abs addr" style="left:194px;top:598px;width:320px">
    <strong>HARBOR LANE LAUNDROMAT</strong>
    1820 B Harbor Lane, San Francisco, CA 94115 (Next to Greenleaf Market)<br>
    <b>OPEN EVERY DAY</b>&nbsp; From 6 am to 10 pm
  </div>
  <div class="abs web-back" style="left:12px;top:657px">www.HarborLaneLaundry.com</div>
  <div class="abs call-back" style="left:210px;top:642px">Call us Now: 415.555.0182</div>
</section>

</body>
</html>
```